tam bor magazine

just need coupons of real customers made for my magazine, I have the layout or temp lets of the magazine i just need the coupons to be made and plug-in. i have examples, of the ads or coupons, I'm sure they will need to redone. and in a section of the magazine their in a church directory. with this section , i need the pic of the pastor plug in with their church information and in do have some ex-samples of that as well. with the websites of the businesses. if you need to grab an image from their site . you'll be able to do so. all of the business are in the upload section , these are small base business so a lot of the ads and logos need redone any way . so i will look at it and let you know.

P.S with the new coupons and logos I'm trying to impress these customers to stay with the magazine

Target Market(s)

small businesses

Requirements
Must have
• good graphics
Should not have
• not pixelated graphics

```html
<!DOCTYPE html>
<html lang="en">
<head>
<meta charset="utf-8">
<title>Church Directory — tam bor magazine</title>
<link href="https://fonts.googleapis.com/css2?family=Arimo:wght@400;700&family=Roboto+Condensed:wght@400;500;700&family=Roboto:wght@400;500;700&family=Zilla+Slab:wght@700&display=swap" rel="stylesheet">
<style>
:root{
  --page:#ffffff;
  --band:#e8e9ea;
  --rule:#9a9a9a;
  --ink:#333333;
  --text:#111111;
  --card-line:#8c8c8c;
  --card-fill:#e9e9ea;
  --peach:#fde8da;
  --lounge:#3a3a3a;
  --orange:#e8661c;
}
*{box-sizing:border-box;margin:0;padding:0}
html,body{width:1200px;height:1200px;overflow:hidden;background:var(--page)}
body{position:relative;font-family:"Roboto",Arial,sans-serif;color:var(--text)}

.masthead{position:absolute;left:0;top:0;width:1200px;height:93px;background:var(--band)}
.masthead::before{content:"";position:absolute;left:144px;right:143px;top:1px;height:1px;background:var(--rule)}
.masthead h1{position:absolute;left:0;right:0;top:18px;text-align:center;font-family:"Roboto",Arial,sans-serif;font-weight:400;font-size:60px;letter-spacing:1px;color:var(--ink);line-height:1}
.masthead h1 b{font-weight:700}
.foot-rule{position:absolute;left:144px;right:143px;top:1197px;height:1px;background:var(--rule)}

/* left ads */
.bakery-ad{position:absolute;left:177px;top:116px;width:285px;height:565px;border:1px solid var(--card-line);font-family:"Arimo",Arial,sans-serif;text-align:center}
.bakery-banner{position:absolute;left:3px;top:11px;width:281px;height:157px;background:linear-gradient(135deg,#e2661f,#c14a14 60%,#9a3410)}
.bakery-mark{position:absolute;left:20px;top:196px;width:245px;height:140px;display:flex;flex-direction:column;align-items:center;justify-content:center;gap:10px}
.bakery-mark .dot{width:62px;height:62px;border-radius:50%;background:var(--orange)}
.bakery-mark span{font-weight:700;font-size:19px;line-height:22px;color:var(--orange);white-space:nowrap}
.bakery-stock{position:absolute;left:18px;top:353px;width:256px;height:68px;background:var(--peach);font-weight:700;font-size:16px;line-height:19.5px;padding-top:5px}
.bakery-shop{position:absolute;left:0;right:0;top:428px;font-size:17.5px;line-height:21px}
.bakery-shop strong{font-weight:700}

.lounge-ad{position:absolute;left:177px;top:702px;width:285px;height:454px;border:1px solid var(--card-line)}
.lounge-title{height:318px;background:var(--lounge);color:#fff;font-family:"Zilla Slab",Georgia,serif;font-weight:700;font-size:38px;line-height:48px;padding:66px 0 0 16px;letter-spacing:.5px}
.lounge-address{text-align:center;font-family:"Arimo",Arial,sans-serif;font-size:25px;line-height:30px;padding-top:16px}

/* church cards */
.card{position:absolute;width:269px;height:200px;border:1px solid var(--card-line);background:#fff;font-family:"Roboto Condensed",Arial,sans-serif;display:flex;flex-direction:column}
.card-head{height:49px;flex:none;display:flex;align-items:center;justify-content:center;text-align:center;font-weight:500;font-size:12px;color:#222;padding:0 3px;white-space:nowrap}
.card-head.tight{font-size:11px;letter-spacing:-.1px}
.card-body{height:102px;flex:none;background:var(--card-fill);position:relative}
.portrait{position:absolute;left:12px;top:6px;width:91px;height:91px;border-radius:50%;border:1.5px solid #8a8a8a;background:radial-gradient(circle at 50% 40%,#a88670,#5b4a44 55%,#d7d7da 56%)}
.info{position:absolute;left:110px;top:10px;right:2px;font-size:10px;line-height:12.5px;color:#222;white-space:nowrap}
.info .name{font-size:12px;font-weight:500;line-height:14.5px;margin-bottom:9px}
.info p{margin-bottom:8px}
.card-foot{flex:1;display:flex;align-items:center;justify-content:center;text-align:center;font-weight:500;font-size:11.5px;line-height:13px;color:#222;padding:0 6px;white-space:nowrap}
.card-foot.split{justify-content:space-between;text-align:left;font-size:8.5px;line-height:10.5px;font-weight:400;padding:0 12px}
.card-foot.split div+div{border-left:1px solid #555;padding-left:6px}
.sans .card-head,.sans .info{font-family:"Roboto",Arial,sans-serif}
.sans .card-head{font-size:12.5px}
.sans .info{font-size:9.5px}
.info.small{font-size:7px;line-height:9px;top:6px}
.info.small .name{margin-bottom:3px}
.info.small p{margin-bottom:4px}
</style>
</head>
<body>

<header class="masthead"><h1>CHURCH <b>DIRECTORY</b></h1></header>

<aside class="bakery-ad">
  <div class="bakery-banner" role="img" aria-label="Hand-lettered bakery banner with the baker's portrait and sweet potato treats"></div>
  <div class="bakery-mark"><div class="dot"></div><span>Crumbhouse Kitchen</span></div>
  <div class="bakery-stock">Products available at Harvest Lane Markets : Elmgrove, Riverbend &amp; Cedar Point.</div>
  <div class="bakery-shop">
    <strong>Bake Shop Location :</strong><br>
    1480 Marlow Avenue,<br>
    Downtown Brookhaven 15390<br>
    555.014.2290<br>
    <strong>www.crumbhousekitchen.com</strong><br>
    TUES- FRIDAY 11 AM - 2 PM
  </div>
</aside>

<aside class="lounge-ad">
  <div class="lounge-title">THE<br>NEW<br>HARLOW'S<br>LOUNGE</div>
  <div class="lounge-address">8120 Wexley Ave<br>Brookhaven<br>PA15390</div>
</aside>

<main>
  <article class="card sans" style="left:478px;top:116px">
    <h2 class="card-head">ZION HILL BAPTIST CHURCH</h2>
    <div class="card-body"><div class="portrait" role="img" aria-label="Portrait of the pastor"></div>
      <div class="info"><div class="name">Reverend<br>Dr. Marcus T. Hale</div><p>3310 Alder Ave, Brookhaven, PA</p><p>(555) 010-4417</p></div></div>
    <div class="card-foot">CHURCH SERVICE SUNDAY 11 AM</div>
  </article>

  <article class="card sans" style="left:758px;top:116px">
    <h2 class="card-head">BETHEL GROVE BAPTIST CHURCH</h2>
    <div class="card-body"><div class="portrait" role="img" aria-label="Portrait of the pastor"></div>
      <div class="info" style="top:16px"><div class="name" style="margin-bottom:7px">Dr. Samuel K. Brooks</div><p>5620 Linden Street Brookhaven<br>PA 15390</p><p>(555) 010-3361</p></div></div>
    <div class="card-foot">SUNDAY WORSHIP SERVICE 10.30 AM</div>
  </article>

  <article class="card" style="left:478px;top:330px">
    <h2 class="card-head tight">GRACE TEMPLE CHURCH BROOKHAVEN (GTC-BRK)</h2>
    <div class="card-body"><div class="portrait" role="img" aria-label="Portrait of the pastor and his wife"></div>
      <div class="info"><div class="name">Reverend<br>Elijah James Porter</div><p>4175 Mill Street, Brookhaven<br>PA. 15390</p><p>(555) 010-2284</p></div></div>
    <div class="card-foot">SUNDAY WORSHIP SERVICE AT 8 AM &amp; 10.45 AM</div>
  </article>

  <article class="card sans" style="left:758px;top:330px">
    <h2 class="card-head">ST. MARK BAPTIST CHURCH</h2>
    <div class="card-body"><div class="portrait" role="img" aria-label="Portrait of the pastor speaking"></div>
      <div class="info" style="top:14px"><div class="name">Pastor, Rev. Linda Moore</div><p>2904 Oak Ave.<br>Brookhaven, Pa</p><p>(555) 010-5523</p></div></div>
    <div class="card-foot">SUNDAY WORSHIP SERVICE @ 10.30 AM<br>SUNDAY SCHOOL 8.30 AM</div>
  </article>

  <article class="card" style="left:478px;top:538px">
    <h2 class="card-head">NEW HORIZON CHRISTIAN FELLOWSHIP</h2>
    <div class="card-body"><div class="portrait" role="img" aria-label="Portrait of the apostle and pastor"></div>
      <div class="info" style="top:6px"><div class="name" style="margin-bottom:5px">Apostle Nathan<br>And<br>Pastor Renee Ward</div><p style="margin-bottom:9px">6215 Hart Street Brookhaven, Pa</p><p>(555) 010-6674</p></div></div>
    <div class="card-foot split"><div>Sunday worship service<br>Sunday service at 11:00 am</div><div>Wednesday bible study at 7.30 pm<br>Saturday prayer at 9:00 am</div></div>
  </article>

  <article class="card" style="left:758px;top:538px">
    <h2 class="card-head">FAIRVIEW ST. MISSIONARY BAPTIST CHURCH</h2>
    <div class="card-body"><div class="portrait" role="img" aria-label="Portrait of the pastor"></div>
      <div class="info"><div class="name">Reverend Dr. Calvin R. Price</div><p>7002 Fairview St. Brookhaven, PA<br>Church Service Join Us Virtually</p><p>(555) 010-7790</p></div></div>
    <div class="card-foot split"><div>Sunday Academy 7.30 am<br>Sunday Worship 9.00 am, 2:00<br>pm 7:00, 10:00 pm</div><div>Mondays 8 am and 12 noon<br>Wednesdays at Noon<br>Saturdays at 10:00 pm</div></div>
  </article>

  <article class="card" style="left:478px;top:751px">
    <h2 class="card-head">REDEMPTION BAPTIST CHURCH</h2>
    <div class="card-body"><div class="portrait" role="img" aria-label="Portrait of the pastor at the pulpit"></div>
      <div class="info" style="top:16px"><div class="name">Dr. Harold W. Jennings Sr.</div><p>915 Kessler Ave, Brookhaven, PA</p><p>(555) 010-8812</p></div></div>
    <div class="card-foot">CHURCH SERVICE SUNDAY 11 AM</div>
  </article>

  <article class="card" style="left:758px;top:751px">
    <h2 class="card-head">CORNERSTONE INTERNATIONAL MINISTRIES</h2>
    <div class="card-body"><div class="portrait" role="img" aria-label="Portrait of the bishop"></div>
      <div class="info" style="top:14px"><div class="name">Bishop Raymond Earl Tate, Jr</div><p style="font-size:9.5px">418 Westbrook Dr. Brookhaven, Pa.</p><p>(555) 010-9935</p></div></div>
    <div class="card-foot">SUNDAY WORSHIP SERVICE 10.30 AM</div>
  </article>

  <article class="card" style="left:478px;top:959px">
    <h2 class="card-head tight">SALEM COMMUNITY MISSIONARY BAPTIST CHURCH</h2>
    <div class="card-body"><div class="portrait" role="img" aria-label="Portrait of the pastor"></div>
      <div class="info small"><div class="name">Reverend Vernon L. Matthews</div><p>5530 RIDGEWAY AVENUE<br>BROOKHAVEN, PA 15390</p><p>555-010-1148 - CHURCH<br>555-010-1193 - FAX</p><p>SUNDAY WORSHIP SERVICE<br>IN-PERSON SUNDAY WORSHIP SERVICE<br>9:00 AM &amp; REPLAY 6:00 PM EST</p></div></div>
    <div class="card-foot" style="font-size:9.5px;line-height:12px;padding:0 2px">WEDNESDAY MIDWEEK ONLY BIBLE STUDY: 2:00 AM - 1:00 PM<br>MIDWEEK CORPORATE PRAYER: 6:00 PM- 7:00 PM</div>
  </article>

  <article class="card" style="left:758px;top:959px">
    <h2 class="card-head">LIVING WORD CENTER CHURCH &nbsp;PASTOR</h2>
    <div class="card-body"><div class="portrait" role="img" aria-label="Portrait of the pastor"></div>
      <div class="info"><div class="name" style="font-size:11.5px;margin-bottom:7px">Reverend Dr. Thomas E. Reed Jr!</div><p style="font-size:9.5px;line-height:12px">Living Word Center Church / 842 N.<br>Ashford Ave./ Brookhaven, Pa 15390/</p><p>(555) 010-4106</p></div></div>
    <div class="card-foot">SUNDAY WORKSHIP SERVICE SUNDAYS@10 AM</div>
  </article>
</main>

<div class="foot-rule"></div>
</body>
</html>
```